Hello,
Just to let you know this is urgent, please.

We are needing an A5 Advertisement for the back page of a calendar booklet. We need it to look sharp and elegant.
To keep it simple we would like to use logo as the graphic.
Attached below is the copy and a dropbox link for a selection of logos and the brand guidelines.
I look forward to receiving your designs.
Many thanks
Marjorie

```html
<!DOCTYPE html>
<html lang="en">
<head>
<meta charset="utf-8">
<title>Ridgeline Polo Club – Season Advertisement</title>
<link rel="stylesheet" href="https://fonts.googleapis.com/css2?family=Lato:wght@400;700;900&display=swap">
<style>
  :root{
    --backdrop:#e6e7e8;
    --ink:#0b0b0b;
    --paper:#ffffff;
    --silver:#a7a9ac;
    --silver-deep:#808285;
    --silver-mark:#7c7d81;
    --gold:#a99562;
    --gold-deep:#6e613b;
    --gold-mark:#71643e;
  }
  *{box-sizing:border-box;margin:0;padding:0}
  html,body{width:878px;height:1200px;overflow:hidden}
  body{background:var(--backdrop);font-family:"Lato",sans-serif;position:relative}
  .ad{position:absolute;left:64px;top:65px;width:749px;height:1070px;background:var(--ink);color:var(--paper)}
  .frame{position:absolute;left:19px;top:19px;width:711px;height:1033px;border:11px solid var(--paper)}
  .brand-name{position:absolute;left:48px;top:70px;width:232px;height:120px;display:flex;align-items:center;justify-content:center;gap:12px;font-size:26px;font-weight:700;letter-spacing:1px;line-height:1.1;text-align:left}
  .brand-name .dot{width:18px;height:18px;border-radius:50%;background:var(--paper);flex:none}
  .title{position:absolute;left:290px;top:100px;width:420px;text-align:center;font-size:50px;font-weight:400;line-height:1.08;letter-spacing:.5px}
  .cup{position:absolute;top:250px;width:318px;height:280px;display:flex;align-items:flex-start;justify-content:center}
  .cup--silver{left:40px;background:var(--silver)}
  .cup--gold{left:390px;background:var(--gold)}
  .cup-mark{position:absolute;left:40px;top:30px;width:238px;height:226px;border-radius:14px}
  .cup--silver .cup-mark{background:var(--silver-mark)}
  .cup--gold .cup-mark{background:var(--gold-mark)}
  .cup-name{position:relative;margin-top:50px;font-size:31px;font-weight:900;line-height:1.13;text-align:center;color:var(--paper)}
  .dates{position:absolute;top:561px;width:318px;height:138px;overflow:hidden;text-align:center}
  .dates--silver{left:40px;background:var(--silver);color:var(--paper)}
  .dates--gold{left:390px;background:var(--gold);color:var(--ink)}
  .dates svg{position:absolute;left:0;top:0}
  .dates .month{position:relative;margin-top:10px;font-size:22px;font-weight:900;line-height:1.1}
  .dates .days{position:relative;font-size:19px;font-weight:700;letter-spacing:.5px;line-height:1.4}
  .dates .grades{position:relative;margin-top:14px;font-size:19px;font-weight:700;letter-spacing:.5px;line-height:1.35;color:var(--ink)}
  .dates--gold .grades{color:var(--paper)}
  .membership{position:absolute;left:0;width:749px;text-align:center}
  .membership .lead{top:0;font-size:22px;font-weight:400;letter-spacing:.5px}
  .membership-lead{top:752px;font-size:22px;letter-spacing:.3px}
  .membership-call{top:784px;font-size:41px;font-weight:900;letter-spacing:.5px}
  .contact{position:absolute;left:48px;top:876px;width:653px;height:138px;background:var(--paper);color:var(--ink);display:flex;align-items:center}
  .contact-brand{width:148px;padding-left:18px;display:flex;align-items:center;gap:6px;font-size:11px;font-weight:700;line-height:1.2}
  .contact-brand .dot{width:10px;height:10px;border-radius:50%;background:var(--ink);flex:none}
  .contact-lines{padding-left:8px}
  .phone{font-size:35px;font-weight:700;line-height:1.1;letter-spacing:.5px}
  .line{font-size:20px;font-weight:700;line-height:1.3;letter-spacing:.3px}
</style>
</head>
<body>
  <article class="ad">
    <div class="frame"></div>

    <div class="brand-name"><span class="dot"></span><span>RIDGELINE<br>POLO CLUB</span></div>
    <h1 class="title">RIDGELINE POLO<br>CLUB</h1>

    <section class="cup cup--silver">
      <div class="cup-mark" role="img" aria-label="Trophy cup silhouette"></div>
      <h2 class="cup-name">RIDGELINE<br>SILVER<br>CUP</h2>
    </section>
    <section class="cup cup--gold">
      <div class="cup-mark" role="img" aria-label="Trophy cup silhouette"></div>
      <h2 class="cup-name">RIDGELINE<br>GOLD<br>CUP</h2>
    </section>

    <div class="dates dates--silver">
      <svg width="318" height="138" viewBox="0 0 318 138" aria-hidden="true">
        <path d="M0 0H318V12C318 40 300 66 272 66H0Z" fill="var(--silver-deep)"/>
      </svg>
      <p class="month">APRIL</p>
      <p class="days">11th, 13th &amp; 14th 2019</p>
      <p class="grades">12, 6 &amp; 2 Goal<br>and Sub Zero</p>
    </div>
    <div class="dates dates--gold">
      <svg width="318" height="138" viewBox="0 0 318 138" aria-hidden="true">
        <path d="M0 138V126C0 96 20 72 50 72H318V138Z" fill="var(--gold-deep)"/>
      </svg>
      <p class="month">OCTOBER</p>
      <p class="days">16th, 17th, 19th &amp; 20th 2019</p>
      <p class="grades">12, 6 &amp; 2 Goal<br>and Sub Zero</p>
    </div>

    <p class="membership membership-lead">PLAYING AND SOCIAL MEMBERSHIPS</p>
    <p class="membership membership-call">NOW AVAILABLE</p>

    <footer class="contact">
      <div class="contact-brand"><span class="dot"></span><span>RIDGELINE<br>POLO CLUB</span></div>
      <div class="contact-lines">
        <p class="phone">(02) 4000 1234</p>
        <p class="line">24 Wattle Lane Kurrajong, NSW</p>
        <p class="line">hello@ridgelinepolo.com | www.ridgelinepolo.com</p>
      </div>
    </footer>
  </article>
</body>
</html>
```